Construction Company Business Card

Business Card Design using new Logo

Contact Information for Business Card

include all company info and website

Requirements
Must have
• Wesley Corman - President
ph. 254-617-0382
Cedar Knoll, TX
wesley@ironmarkframing.com
www.ironmarkframing.com

```html
<!DOCTYPE html>
<html lang="en">
<head>
<meta charset="utf-8">
<title>Ironmark Framing – Business Card</title>
<link href="https://fonts.googleapis.com/css2?family=Montserrat:wght@400;500;600;700&display=swap" rel="stylesheet">
<style>
  :root {
    --backdrop: #2b2b2d;
    --brand-red: #c9222b;
    --brand-red-light: #d63a42;
    --card-white: #ffffff;
    --rim-grey: #b9babe;
    --logo-grey: #a7a8ac;
    --text-white: #ffffff;
  }
  * { margin: 0; padding: 0; box-sizing: border-box; }
  html, body {
    width: 1200px; height: 881px; overflow: hidden;
    background: var(--backdrop);
    font-family: "Montserrat", sans-serif;
  }
  .canvas { position: relative; width: 1200px; height: 881px; }
  .card {
    position: absolute; width: 620px; height: 354px;
    border-radius: 28px; overflow: hidden;
    box-shadow: 0 18px 40px rgba(0,0,0,.45);
  }
  .card-front {
    left: 90px; top: 60px;
    background: linear-gradient(100deg, var(--brand-red) 0%, var(--brand-red-light) 35%, var(--brand-red) 60%);
    display: flex; align-items: center; justify-content: center;
  }
  .brand-lockup { display: flex; align-items: center; gap: 12px; white-space: nowrap; }
  .brand-square { width: 18px; height: 18px; background: currentColor; flex: none; }
  .brand-name {
    font-weight: 600; font-size: 34px; letter-spacing: 4px;
    text-transform: uppercase;
  }
  .card-front .brand-lockup { color: var(--text-white); }
  .card-back {
    left: 490px; top: 462px;
    background: linear-gradient(100deg, var(--brand-red) 0%, var(--brand-red-light) 30%, var(--brand-red) 55%);
  }
  .card-back .sweep { position: absolute; inset: 0; }
  .card-back .brand-lockup {
    position: absolute; right: 34px; top: 82px; color: var(--logo-grey); gap: 8px;
  }
  .card-back .brand-name { font-size: 18px; letter-spacing: 2.5px; }
  .card-back .brand-square { background: var(--brand-red); width: 11px; height: 11px; }
  .contact {
    position: absolute; left: 38px; bottom: 24px; color: var(--text-white);
  }
  .contact-name {
    font-weight: 700; font-size: 30px; letter-spacing: 1.5px; text-transform: uppercase; line-height: 1;
    white-space: nowrap;
  }
  .contact-title { font-size: 18px; letter-spacing: 1px; margin: 6px 0 12px; }
  .contact-list { list-style: none; font-size: 17px; letter-spacing: .3px; }
  .contact-list li { display: flex; align-items: center; gap: 10px; line-height: 25px; white-space: nowrap; }
  .contact-list svg { width: 14px; height: 14px; flex: none; }
</style>
</head>
<body>
<main class="canvas">
  <section class="card card-front" aria-label="Card front">
    <div class="brand-lockup">
      <span class="brand-square"></span>
      <span class="brand-name">Ironmark Framing</span>
    </div>
  </section>

  <section class="card card-back" aria-label="Card back">
    <svg class="sweep" viewBox="0 0 620 354" preserveAspectRatio="none" aria-hidden="true">
      <path d="M286 0 C318 204 445 266 620 270 L620 0 Z" fill="var(--rim-grey)"/>
      <path d="M300 0 C330 190 450 250 620 258 L620 0 Z" fill="var(--card-white)"/>
    </svg>
    <div class="brand-lockup">
      <span class="brand-square"></span>
      <span class="brand-name">Ironmark Framing</span>
    </div>
    <div class="contact">
      <h1 class="contact-name">Wesley Corman</h1>
      <p class="contact-title">President</p>
      <ul class="contact-list">
        <li><svg viewBox="0 0 16 16"><path d="M4 1l3 3-2 2c1 2 3 4 5 5l2-2 3 3-2 3C7 15 1 9 1 3z" fill="none" stroke="#fff" stroke-width="1.5"/></svg>254-617-0382</li>
        <li><svg viewBox="0 0 16 16"><rect x="1" y="3" width="14" height="10" rx="1" fill="none" stroke="#fff" stroke-width="1.5"/><path d="M1 4l7 5 7-5" fill="none" stroke="#fff" stroke-width="1.5"/></svg>wesley@ironmarkframing.com</li>
        <li><svg viewBox="0 0 16 16"><circle cx="8" cy="8" r="6.5" fill="none" stroke="#fff" stroke-width="1.3"/><ellipse cx="8" cy="8" rx="3" ry="6.5" fill="none" stroke="#fff" stroke-width="1.2"/><path d="M1.5 8h13M3 4.5h10M3 11.5h10" stroke="#fff" stroke-width="1.1"/></svg>www.ironmarkframing.com</li>
        <li><svg viewBox="0 0 16 16"><path d="M8 15s5-5.5 5-9a5 5 0 0 0-10 0c0 3.5 5 9 5 9z" fill="#fff"/><circle cx="8" cy="6" r="2" fill="var(--brand-red)"/></svg>Cedar Knoll, TX</li>
      </ul>
    </div>
  </section>
</main>
</body>
</html>
```